Web Design Business Card

I need a new business card designed, we recently rebranded and I need to get a fresh design to match our new logo, colours and branding.

Details:

Dorian Keeble | Founder & CEO
Address: 7 Fernhollow Lane, #04-09 Maplecrest Vale, Singapore 583104
Tel: +65 93468120
Web: www.plumtrove.com.sg
hello@plumtrove.com.sg

I've attached my old card as well

Requirements
Must have
• Front and Back
Interesting use of logo
Correct use of colour scheme

```html
<!DOCTYPE html>
<html lang="en">
<head>
<meta charset="utf-8">
<title>Plumtrove Business Card – Front and Back</title>
<link rel="stylesheet" href="https://fonts.googleapis.com/css2?family=Montserrat:wght@300;400;700&display=swap">
<style>
  :root {
    --page-bg: #dcdcdc;
    --card-white: #efeff0;
    --band-white: #ececec;
    --blue-deep: #1560c8;
    --blue-mid: #2a8ee0;
    --blue-light: #3cb0e6;
    --accent-blue: #2aa0d8;
    --ink-grey: #5f5f5f;
    --ink-soft: #6e6e6e;
  }
  * { box-sizing: border-box; margin: 0; padding: 0; }
  html, body {
    width: 1200px; height: 900px; overflow: hidden;
    background: var(--page-bg);
    font-family: "Montserrat", Arial, sans-serif;
  }
  .sheet {
    width: 1200px; height: 900px;
    display: flex; flex-direction: column; align-items: center; justify-content: center;
    gap: 40px;
  }
  .card {
    position: relative;
    width: 700px; height: 400px;
    overflow: hidden;
    box-shadow: 0 6px 18px rgba(0,0,0,.18);
  }

  /* Front */
  .card--front { background: var(--card-white); }
  .front-pattern {
    position: absolute; inset: 0;
    background: linear-gradient(125deg, var(--blue-deep) 0%, var(--blue-mid) 45%, var(--blue-light) 70%, var(--blue-deep) 100%);
  }
  .front-band {
    position: absolute; left: 0; right: 0; top: 140px; height: 112px;
    background: var(--band-white);
    display: flex; align-items: center; justify-content: center; gap: 18px;
  }
  .brand-dot {
    width: 72px; height: 72px; border-radius: 50%;
    background: var(--accent-blue);
  }
  .brand-text { display: flex; flex-direction: column; }
  .brand-name {
    font-weight: 700; font-size: 54px; line-height: 1;
    color: var(--ink-grey); letter-spacing: -0.5px;
  }
  .brand-tagline {
    margin-top: 4px;
    font-weight: 700; font-size: 10.5px; letter-spacing: 1.6px;
    color: var(--accent-blue); text-transform: uppercase;
  }

  /* Back */
  .card--back { background: var(--card-white); }
  .back-circle {
    position: absolute; left: 95px; top: 118px;
    width: 150px; height: 150px; border-radius: 50%;
    background: linear-gradient(135deg, var(--accent-blue), var(--blue-mid));
  }
  .back-url {
    position: absolute; left: 48px; bottom: 40px;
    font-size: 17px; font-weight: 400; color: var(--accent-blue);
  }
  .details {
    position: absolute; left: 380px; top: 48px; right: 0;
    color: var(--ink-soft);
  }
  .person-name {
    font-weight: 300; font-size: 26px; letter-spacing: 1px;
    text-transform: uppercase; color: var(--ink-grey);
  }
  .person-role { font-weight: 300; font-size: 17px; margin-top: 2px; }
  .rule {
    height: 1.5px; background: var(--accent-blue);
    margin-top: 16px; margin-bottom: 28px;
  }
  .contact { list-style: none; font-size: 14px; font-weight: 300; line-height: 1.5; }
  .contact-label {
    display: inline-block; width: 18px;
    color: var(--accent-blue); font-weight: 400;
  }
  .address {
    margin-top: 22px; margin-left: 18px;
    font-size: 14px; font-weight: 300; line-height: 1.5; font-style: normal;
  }
</style>
</head>
<body>
<main class="sheet">
  <section class="card card--front" aria-label="Card front">
    <div class="front-pattern" role="img" aria-label="Blue low-poly geometric pattern"></div>
    <div class="front-band">
      <span class="brand-dot"></span>
      <div class="brand-text">
        <span class="brand-name">plumtrove</span>
        <span class="brand-tagline">Web Design &amp; Consultancy</span>
      </div>
    </div>
  </section>

  <section class="card card--back" aria-label="Card back">
    <span class="back-circle"></span>
    <p class="back-url">www.plumtrove.com.sg</p>
    <div class="details">
      <h1 class="person-name">Dorian Keeble</h1>
      <p class="person-role">Founder &amp; CEO</p>
      <div class="rule"></div>
      <ul class="contact">
        <li><span class="contact-label">T</span>+65 93468120</li>
        <li><span class="contact-label">E</span>hello@plumtrove.com.sg</li>
      </ul>
      <address class="address">
        7 Fernhollow Lane,<br>
        #04-09 Maplecrest Vale,<br>
        Singapore 583104
      </address>
    </div>
  </section>
</main>
</body>
</html>
```